- Redesign our business card
- Logo remains unchanged
- Current business card attached

Target Market(s)

We are a property management company

Industry/Entity Type

Business

```html
<!DOCTYPE html>
<html lang="en">
<head>
<meta charset="utf-8">
<title>Harlow Property – Business Card</title>
<link rel="stylesheet" href="https://fonts.googleapis.com/css2?family=League+Spartan:wght@700&family=Didact+Gothic&family=Roboto+Condensed:wght@300&display=swap">
<style>
  :root {
    --paper: #ffffff;
    --ink: #222222;
    --cream: #eeead8;
    --olive: #c6c39f;
    --grey: #b9b9b6;
  }
  html, body {
    margin: 0;
    padding: 0;
    overflow: hidden;
    background: var(--paper);
  }
  .card {
    position: relative;
    width: 1200px;
    height: 667px;
    background: var(--paper);
    overflow: hidden;
    color: var(--ink);
  }
  .card__backdrop {
    position: absolute;
    left: 180px;
    top: 30px;
    width: 860px;
    height: 620px;
    border-radius: 10px;
    background: linear-gradient(90deg, var(--cream) 0%, var(--olive) 50%, var(--grey) 100%);
  }
  .line {
    position: absolute;
    left: 15px;
    width: 1200px;
    margin: 0;
    white-space: nowrap;
    line-height: 1;
    text-align: center;
  }
  .services {
    top: 160px;
    left: 78px;
    width: 1093px;
    display: flex;
    justify-content: space-between;
    font-family: "Roboto Condensed", sans-serif;
    font-weight: 300;
    font-size: 34px;
    text-align: left;
  }
  .name {
    top: 283px;
    left: 9px;
    font-family: "League Spartan", sans-serif;
    font-weight: 700;
    font-size: 40px;
    letter-spacing: 1px;
  }
  .role {
    top: 333px;
    left: 8px;
    font-family: "Didact Gothic", sans-serif;
    font-size: 33px;
  }
  .contact {
    font-family: "Didact Gothic", sans-serif;
    font-size: 31px;
    letter-spacing: 0.5px;
  }
  .contact--po     { top: 436px; }
  .contact--street { top: 484px; }
  .contact--phone  { top: 532px; }
  .contact--web    { top: 580px; }
  .gap { display: inline-block; width: 34px; }
</style>
</head>
<body>
  <div class="card">
    <div class="card__backdrop" role="img" aria-label="Soft cream, olive and grey colour field behind the card details"></div>

    <p class="line services"><span>Strata Management</span><span>|</span><span>Community Management</span><span>|</span><span>Property Management</span></p>

    <h1 class="line name">DANIEL HARLOW</h1>
    <p class="line role">Licensed Strata Manager</p>

    <p class="line contact contact--po">PO BOX 48, BRIGHTWATER NSW 2031</p>
    <p class="line contact contact--street">12/6-18 ELMWOOD STREET MARLOWE NSW 2042</p>
    <p class="line contact contact--phone">T: 02 9384 1170<span class="gap"></span>F: 02 9384 2295<span class="gap"></span>M: 0431 608 372</p>
    <p class="line contact contact--web">E: info@harlowproperty.com.au<span class="gap"></span>www.harlowproperty.com.au</p>
  </div>
</body>
</html>
```